Business Card Design

We are looking for a double sided business card.

On one side would be our logo

On the Other Side

Martin Kolby
Sales and Marketing

Phone/Text Logo and 530-418-2763
Email Logo and info@plumvalepets.com
Website Logo and www.plumvalepets.com
Facebook Logo and plumvale pets
Instagram Logo and plumvale_pets

Target Market(s)

Pet owners

Contact Information for Business Card

In project description

Requirements
Must have
• Logo

```html
<!DOCTYPE html>
<html lang="en">
<head>
<meta charset="utf-8">
<title>Plumvale Pets – Business Card</title>
<link href="https://fonts.googleapis.com/css2?family=Arimo:wght@400;700&display=swap" rel="stylesheet">
<style>
  :root {
    --page: #d9d9d9;
    --card-dark: #2f2f31;
    --silver: #cfcfcf;
    --orange: #ee7f24;
    --orange-glow: #f2ab2c;
    --ink-light: #ffffff;
    --brand: #d8d8d8;
  }
  * { margin: 0; padding: 0; box-sizing: border-box; }
  html, body {
    width: 1200px; height: 874px; overflow: hidden;
    background: var(--page);
    font-family: "Arimo", Arial, sans-serif;
  }
  .sheet {
    width: 1200px; height: 874px;
    display: flex; flex-direction: column; align-items: center; justify-content: center;
    gap: 30px;
  }
  .card {
    position: relative;
    width: 680px; height: 388px;
    border-radius: 22px;
    background: var(--card-dark);
    overflow: hidden;
    box-shadow: 0 6px 18px rgba(0,0,0,.25);
  }
  .brand {
    display: flex; align-items: center; gap: 14px;
    color: var(--brand);
    font-weight: 700;
    letter-spacing: 2px;
    text-transform: uppercase;
  }
  .brand-dot {
    width: 22px; height: 22px; border-radius: 50%;
    background: var(--orange);
    flex: none;
  }
  .card--logo { display: flex; align-items: center; justify-content: center; }
  .card--logo .brand { font-size: 46px; }

  .card--contact .panel { position: absolute; inset: 0; }
  .card--contact .brand {
    position: absolute; left: 40px; top: 150px;
    font-size: 30px; line-height: 1.1; gap: 12px;
  }
  .card--contact .brand-dot { width: 18px; height: 18px; }
  .brand-name { display: flex; flex-direction: column; }

  .contact {
    position: absolute; left: 400px; top: 78px;
    color: var(--ink-light);
  }
  .contact-name { font-size: 27px; font-weight: 700; letter-spacing: .5px; text-transform: uppercase; }
  .contact-role { font-size: 16px; margin-top: 2px; }
  .contact-address { font-size: 17px; line-height: 1.3; margin-top: 16px; }
  .contact-list { list-style: none; margin-top: 14px; font-size: 16px; line-height: 1.45; }
  .contact-list li { display: flex; align-items: center; gap: 10px; }
  .contact-list svg { width: 14px; height: 14px; flex: none; }
</style>
</head>
<body>
<main class="sheet">
  <section class="card card--logo" aria-label="Card front">
    <div class="brand"><span class="brand-dot"></span>Plumvale Pets</div>
  </section>

  <section class="card card--contact" aria-label="Card back">
    <svg class="panel" viewBox="0 0 680 388" preserveAspectRatio="none" aria-hidden="true">
      <defs>
        <radialGradient id="orangeGlow" cx="0.45" cy="0.45" r="0.6">
          <stop offset="0" stop-color="#f2ab2c"/>
          <stop offset="1" stop-color="#ee7f24"/>
        </radialGradient>
      </defs>
      <path d="M345,0 C285,40 315,200 285,300 C270,350 235,380 212,388 L680,388 L680,0 Z" fill="#cfcfcf"/>
      <path d="M365,0 C305,40 335,200 305,300 C290,350 255,380 232,388 L680,388 L680,0 Z" fill="url(#orangeGlow)"/>
    </svg>

    <div class="brand">
      <span class="brand-dot"></span>
      <span class="brand-name"><span>Plumvale</span><span>Pets</span></span>
    </div>

    <div class="contact">
      <p class="contact-name">Martin Kolby</p>
      <p class="contact-role">Sales and Marketing</p>
      <p class="contact-address">412 Alder Court<br>Fairbanks, Canada 20918</p>
      <ul class="contact-list">
        <li>
          <svg viewBox="0 0 16 16" aria-label="Phone"><path fill="#fff" d="M3 1l3 3-1.5 2a9 9 0 0 0 5.5 5.5L12 10l3 3-2 2C7 15 1 9 1 3z"/></svg>
          530-418-2763
        </li>
        <li>
          <svg viewBox="0 0 16 16" aria-label="Email"><rect x="1" y="3" width="14" height="10" fill="#fff"/><path d="M1 3l7 6 7-6" fill="none" stroke="#ee7f24" stroke-width="1.4"/></svg>
          info@plumvalepets.com
        </li>
        <li>
          <svg viewBox="0 0 16 16" aria-label="Website"><circle cx="8" cy="8" r="7" fill="#fff"/><path d="M1 8h14M8 1c-3 3-3 11 0 14M8 1c3 3 3 11 0 14" fill="none" stroke="#ee7f24" stroke-width="1"/></svg>
          www.plumvalepets.com
        </li>
        <li>
          <svg viewBox="0 0 16 16" aria-label="Social page"><circle cx="8" cy="8" r="6" fill="#fff"/></svg>
          plumvale pets
        </li>
        <li>
          <svg viewBox="0 0 16 16" aria-label="Social handle"><rect x="2" y="2" width="12" height="12" fill="#fff"/></svg>
          plumvale_pets
        </li>
      </ul>
    </div>
  </section>
</main>
</body>
</html>
```